Business Card Design

Design new business card using new logo attached and some details as old business card, which is also attached.

Industry/Entity Type

Business

```html
<!DOCTYPE html>
<html lang="en">
<head>
<meta charset="utf-8">
<title>Whitfield CPA – Business Card</title>
<link rel="stylesheet" href="https://fonts.googleapis.com/css2?family=Cinzel:wght@400;600;700&family=Arimo:wght@400;700&display=swap">
<style>
  :root {
    --page: #e6e7ea;
    --navy: #141485;
    --navy-deep: #0a0a5e;
    --navy-text: #1b1b7a;
    --silver: #d9dbe3;
    --white: #ffffff;
    --card-white: #f7f7f8;
    --grey-text: #6c6e74;
    --grey-line: #8d8f95;
    --faint: rgba(120, 120, 170, 0.16);
  }
  * { box-sizing: border-box; margin: 0; padding: 0; }
  html, body { width: 1200px; height: 1200px; overflow: hidden; }
  body {
    background: var(--page);
    display: flex;
    flex-direction: column;
    align-items: center;
    justify-content: center;
    gap: 44px;
    font-family: "Arimo", Arial, sans-serif;
  }
  .card {
    position: relative;
    width: 900px;
    height: 514px;
    overflow: hidden;
    box-shadow: 0 10px 30px rgba(0,0,0,0.18);
  }

  /* Back of card */
  .card--back {
    background: linear-gradient(160deg, var(--navy) 0%, var(--navy-deep) 100%);
  }
  .lockup {
    position: absolute;
    display: flex;
    align-items: center;
  }
  .card--back .lockup { left: 200px; top: 200px; }
  .lockup__name {
    font-family: "Cinzel", Georgia, serif;
    font-weight: 700;
    font-size: 48px;
    letter-spacing: 1px;
    display: flex;
    align-items: center;
    gap: 12px;
  }
  .lockup__square { width: 14px; height: 14px; display: inline-block; }
  .lockup__rule { width: 1px; height: 78px; margin: 0 18px; }
  .lockup__services {
    font-family: "Cinzel", Georgia, serif;
    font-weight: 600;
    font-size: 22px;
    line-height: 1.05;
    letter-spacing: 0.5px;
  }
  .lockup__person {
    font-family: "Cinzel", Georgia, serif;
    font-size: 12px;
    letter-spacing: 1px;
    margin-top: 4px;
  }
  .card--back .lockup__name,
  .card--back .lockup__services,
  .card--back .lockup__person { color: var(--silver); }
  .card--back .lockup__square { background: var(--silver); }
  .card--back .lockup__rule { background: rgba(255,255,255,0.5); }
  .back__url {
    position: absolute;
    right: 48px;
    bottom: 36px;
    color: var(--white);
    font-size: 16px;
    letter-spacing: 0.3px;
  }
  .back__url b { font-weight: 700; }

  /* Front of card */
  .card--front {
    background: linear-gradient(180deg, var(--white) 0%, var(--card-white) 100%);
  }
  .card--front .lockup { right: 44px; top: 40px; }
  .card--front .lockup__name { font-size: 38px; color: var(--navy-text); }
  .card--front .lockup__square { background: var(--grey-line); width: 12px; height: 12px; }
  .card--front .lockup__rule { background: var(--grey-line); height: 60px; margin: 0 12px; }
  .card--front .lockup__services { font-size: 16px; color: var(--navy-text); }
  .card--front .lockup__person { font-size: 9px; color: var(--grey-text); }

  .watermark {
    position: absolute;
    right: 30px;
    top: 170px;
    font-family: "Cinzel", Georgia, serif;
    font-weight: 700;
    font-size: 92px;
    color: var(--faint);
    letter-spacing: 2px;
  }
  .title {
    position: absolute;
    left: 80px;
    top: 150px;
    width: 740px;
  }
  .title__name {
    font-family: "Cinzel", Georgia, serif;
    font-weight: 700;
    font-size: 42px;
    color: var(--navy-text);
    letter-spacing: 1.5px;
    text-align: center;
    padding-bottom: 6px;
    border-bottom: 1px solid var(--grey-line);
  }
  .title__sub {
    display: flex;
    justify-content: space-between;
    color: var(--grey-text);
    font-size: 18px;
    margin-top: 8px;
    padding: 0 6px;
  }
  .address {
    position: absolute;
    right: 60px;
    top: 262px;
    text-align: right;
    color: var(--grey-text);
    font-size: 19px;
    line-height: 1.3;
  }
  .contacts {
    position: absolute;
    left: 80px;
    bottom: 46px;
    color: var(--grey-text);
    font-size: 19px;
    line-height: 1.35;
  }
  .contact { display: flex; align-items: center; gap: 12px; }
  .contact svg { width: 14px; height: 14px; flex: none; }
  .contacts__url { margin-top: 4px; }
  .contacts__url b { color: var(--navy-text); }
</style>
</head>
<body>

  <section class="card card--back" aria-label="Business card back">
    <div class="lockup">
      <div class="lockup__name"><span class="lockup__square"></span>Whitfield</div>
      <span class="lockup__rule"></span>
      <div>
        <div class="lockup__services">Tax, Accounting &amp;<br>Advisory Services</div>
        <div class="lockup__person">Daniel R. Whitfield, CPA, PA</div>
      </div>
    </div>
    <div class="back__url">www.<b>whitfieldcpa</b>.com</div>
  </section>

  <section class="card card--front" aria-label="Business card front">
    <div class="lockup">
      <div class="lockup__name"><span class="lockup__square"></span>Whitfield</div>
      <span class="lockup__rule"></span>
      <div>
        <div class="lockup__services">Tax, Accounting &amp;<br>Advisory Services</div>
        <div class="lockup__person">Daniel R. Whitfield, CPA, PA</div>
      </div>
    </div>

    <div class="watermark" aria-hidden="true">Whitfield</div>

    <div class="title">
      <h1 class="title__name">Daniel R. Whitfield, CPA, PA</h1>
      <div class="title__sub">
        <span>A Florida Professional Association</span>
        <span>Tax, Accounting &amp; Advisory Services</span>
      </div>
    </div>

    <address class="address" style="font-style:normal">
      240 Harbor Point Ave.<br>
      Seabrook Beach, FL 32400
    </address>

    <div class="contacts">
      <div class="contact">
        <svg viewBox="0 0 16 16" aria-hidden="true"><path fill="#2d6fc0" d="M3.5 1.5l2.4 2.6-1.3 1.8c.9 2 2.5 3.6 4.5 4.5l1.8-1.3 2.6 2.4-1.6 2.2C6.8 13.5 2.5 9.2 1.3 3.1z"/></svg>
        <span>(850) 555 -0148</span>
      </div>
      <div class="contact">
        <svg viewBox="0 0 16 16" aria-hidden="true"><rect x="4" y="1" width="8" height="14" rx="1.5" fill="none" stroke="#2d6fc0" stroke-width="1.6"/><rect x="6" y="3" width="4" height="7" fill="#2d6fc0"/></svg>
        <span>(256) 555 - 0193</span>
      </div>
      <div class="contact">
        <svg viewBox="0 0 16 16" aria-hidden="true"><rect x="1.5" y="3.5" width="13" height="9" fill="none" stroke="#2d6fc0" stroke-width="1.4"/><path d="M1.5 3.5L8 9l6.5-5.5" fill="none" stroke="#2d6fc0" stroke-width="1.4"/></svg>
        <span>dan@whitfieldcpa.com</span>
      </div>
      <div class="contacts__url">www.<b>whitfieldcpa</b>.com</div>
    </div>
  </section>

</body>
</html>
```